Varden Homes needs a stationery design

I need a stationary design for my new custom home building company. Our company deals with very high end and luxurious homes so i need a stationary design that shows strength, elegance, and trust.
The final version should be trendy, clean... only 2 colours (green + grey/black) and professional.
#1: Business Cards (design on 2 sides)
#2: Letterhead (word format)
#3: Cover Page and back cover for proposals
#4: Envelopes,
#5: Thank You card,
#6: Presentation Folder
Logo is attached. Logo can be reversed out (will attach once available). Logo can be stacked or horizontal (provided as horizontal).
The business cards need to be two sided with the company logo and website on the front (www.vardenhomes-example.com and contact info on the back.
The contact info can be made up temporarily and once the final design is chosen, i will provide you with all the correct contact information during the revision stage.
id like to see examples with black, white, blue, red, purple. (You should not try to use all these in one design)
I have attached my company's logo in 3 different colours and a few sample business cards that i found on the internet. I would like to see unique designs though, don't try to imitate the examples
Updates
Dear designers,
I have also attached the .eps and ai files for the 3 different coloured logos.
Please notify me if you need anything else to complete your work
Best Regards,
Varden

```html
<!DOCTYPE html>
<html lang="en">
<head>
<meta charset="utf-8">
<title>Varden Homes – Stationery</title>
<link rel="stylesheet" href="https://fonts.googleapis.com/css2?family=Open+Sans:wght@400;600;700&display=swap">
<style>
  :root {
    --navy: #212a63;
    --red: #ed1c24;
    --purple: #6a4c9c;
    --black: #000000;
    --card-grey: #e6e6e8;
    --paper: #ffffff;
    --ink: #1b1b1b;
    --page: #ffffff;
    --stage-cream: #fbf0d6;
    --stage-grey: #6d6e70;
  }
  * { box-sizing: border-box; margin: 0; padding: 0; }
  html, body { width: 1200px; height: 1000px; overflow: hidden; }
  body {
    background: var(--page);
    font-family: "Open Sans", Arial, sans-serif;
    color: var(--ink);
    position: relative;
  }

  /* Presentation stage */
  .stage-top {
    position: absolute;
    left: 140px; top: 138px;
    width: 940px; height: 507px;
    background: linear-gradient(180deg, var(--stage-cream), #fdf6e6);
  }
  .stage-bottom {
    position: absolute;
    left: 140px; top: 645px;
    width: 940px; height: 256px;
    background: var(--stage-grey);
  }

  /* Business card – front */
  .card {
    position: absolute;
    width: 255px;
    height: 157px;
    background: var(--card-grey);
    overflow: hidden;
  }
  .card-band {
    height: 78px;
    display: flex;
    align-items: center;
    justify-content: center;
  }
  .wordmark {
    font-weight: 700;
    letter-spacing: 2px;
    text-transform: uppercase;
    line-height: 1;
    white-space: nowrap;
  }
  .card-band .wordmark { color: #fff; font-size: 22px; }
  .card-web {
    padding-top: 23px;
    text-align: center;
    font-size: 12.5px;
    line-height: 16px;
    color: var(--ink);
  }
  .band-navy { background: var(--navy); }
  .band-red { background: var(--red); }
  .band-purple { background: var(--purple); }
  .band-black { background: var(--black); }

  .card-front { left: 178px; top: 308px; }

  /* Business card – back */
  .card-back {
    left: 178px; top: 480px;
    height: 155px;
    background: var(--paper);
  }
  .card-back .wordmark {
    position: absolute;
    left: 26px; top: 62px;
    color: var(--navy);
    font-size: 14px;
    line-height: 1.15;
    letter-spacing: 2px;
    white-space: normal;
    width: 90px;
    text-align: center;
  }
  .holder {
    position: absolute;
    left: 151px; top: 22px;
  }
  .holder-name { font-size: 8px; font-weight: 700; letter-spacing: .2px; }
  .holder-role { font-size: 7px; margin-top: 1px; }
  .contact-list {
    position: absolute;
    left: 126px; top: 58px;
    list-style: none;
  }
  .contact-list li {
    display: flex;
    align-items: center;
    gap: 6px;
    height: 23px;
    font-size: 5px;
  }
  .contact-list svg { width: 20px; height: 16px; fill: var(--navy); }

  /* Letterhead */
  .letterhead {
    position: absolute;
    left: 620px; top: 150px;
    width: 372px;
    height: 482px;
    background: var(--paper);
  }
  .letterhead-logo {
    position: absolute;
    left: 34px; top: 30px;
    width: 116px; height: 36px;
    background: var(--navy);
    display: flex;
    align-items: center;
    justify-content: center;
  }
  .letterhead-logo .wordmark { color: #fff; font-size: 11px; letter-spacing: 1px; }
  .letterhead-address {
    position: absolute;
    left: 34px; top: 84px;
    font-size: 7px;
    line-height: 1.35;
    font-style: normal;
  }

  /* Colour variants */
  .variants { position: absolute; left: 0; top: 685px; width: 1200px; }
  .variant-1 { left: 181px; top: 0; }
  .variant-2 { left: 483px; top: 0; }
  .variant-3 { left: 786px; top: 0; }
</style>
</head>
<body>

  <div class="stage-top" aria-hidden="true"></div>
  <div class="stage-bottom" aria-hidden="true"></div>

  <section class="letterhead" aria-label="Letterhead">
    <div class="letterhead-logo"><span class="wordmark">Varden Homes</span></div>
    <address class="letterhead-address">
      Address: 1234 Harlow Lane<br>
      Brookfield<br>
      Tel: 0555 0123<br>
      Mobile: 0555 0198 7654<br>
      email: info@vardenhomes-example.com
    </address>
  </section>

  <section class="card card-front" aria-label="Business card front">
    <div class="card-band band-navy"><span class="wordmark">Varden Homes</span></div>
    <div class="card-web">www.vardenhomes-example.com</div>
  </section>

  <section class="card card-back" aria-label="Business card back">
    <span class="wordmark">Varden Homes</span>
    <div class="holder">
      <p class="holder-name">DANIEL HARROW</p>
      <p class="holder-role">Project Manager</p>
    </div>
    <ul class="contact-list">
      <li>
        <svg viewBox="0 0 20 16" aria-hidden="true"><path d="M10 1 1 8h3v7h12V8h3z"/></svg>
        Address
      </li>
      <li>
        <svg viewBox="0 0 20 16" aria-hidden="true"><path d="M3 6c0-3 14-3 14 0v2h-4V6.5c-2-.6-4-.6-6 0V8H3z"/><rect x="5" y="9" width="10" height="5" rx="1"/></svg>
        Telephone
      </li>
      <li>
        <svg viewBox="0 0 20 16" aria-hidden="true"><rect x="6" y="0" width="8" height="16" rx="1.5"/><rect x="7.5" y="2" width="5" height="9" fill="#fff"/></svg>
        Mobile
      </li>
      <li>
        <svg viewBox="0 0 20 16" aria-hidden="true"><rect x="1" y="2" width="18" height="12"/><path d="M1 2l9 7 9-7" fill="none" stroke="#fff" stroke-width="1.5"/></svg>
        e-mail
      </li>
    </ul>
  </section>

  <div class="variants">
    <section class="card variant-1" aria-label="Business card front, red">
      <div class="card-band band-red"><span class="wordmark">Varden Homes</span></div>
      <div class="card-web">www.vardenhomes-example.com</div>
    </section>
    <section class="card variant-2" aria-label="Business card front, purple">
      <div class="card-band band-purple"><span class="wordmark">Varden Homes</span></div>
      <div class="card-web">www.vardenhomes-example.com</div>
    </section>
    <section class="card variant-3" aria-label="Business card front, black">
      <div class="card-band band-black"><span class="wordmark">Varden Homes</span></div>
      <div class="card-web">www.vardenhomes-example.com</div>
    </section>
  </div>

</body>
</html>
```